Presentation PDF covers

Produce a PDF front cover & Back cover for PDF sales proposal - will also need to be able to print as a presentation folder if the customer requires a hard copy. The PDF & Covers will need to be A4 portrait with the image (main picture as large as possible) The company Logo to be in a corner with other logos displayed on front.

the rear cover to just have company details on back -

```html
<!DOCTYPE html>
<html lang="en">
<head>
<meta charset="utf-8">
<title>Voltline Services – Sales Proposal Covers</title>
<link rel="stylesheet" href="https://fonts.googleapis.com/css2?family=Oswald:wght@500;700&family=Source+Sans+3:wght@400;600;700&display=swap">
<style>
  :root{
    --navy:#0b1640;
    --green:#6dc38b;
    --yellow:#ffcd05;
    --pale-yellow:#fcf37a;
    --blue:#4a8fd0;
    --grey-bg:#e6e7e9;
    --charcoal:#4d4d4f;
    --gold:#d9b23a;
    --white:#ffffff;
    --badge-dark:#1f1f22;
    --badge-red:#e8413c;
    --badge-blue:#2f5da8;
    --badge-purple:#7b3f98;
    --badge-orange:#f0a020;
    --badge-grey:#8a8c90;
  }
  *{box-sizing:border-box;margin:0;padding:0}
  html,body{width:1200px;height:911px;overflow:hidden;background:var(--grey-bg)}
  body{position:relative;font-family:"Source Sans 3",Arial,sans-serif;color:var(--navy)}
  .spread-divider{position:absolute;left:593px;top:0;width:13px;height:911px;background:var(--white)}
  .cover-label{position:absolute;top:30px;width:539px;text-align:center;font-weight:400;font-size:40px;letter-spacing:1px;color:var(--navy)}
  .cover-label--back{left:27px}
  .cover-label--front{left:634px}
  .page{position:absolute;top:88px;width:539px;height:762px;overflow:hidden;background:var(--navy)}
  .page--back{left:27px}
  .page--front{left:634px}
  .page-art{position:absolute;inset:0;width:100%;height:100%}

  /* shared brand name */
  .brand-mark{display:flex;align-items:center;justify-content:center;gap:8px;font-weight:700;color:var(--charcoal);line-height:40px}
  .brand-mark__dot{width:24px;height:24px;border-radius:50%;background:var(--yellow)}

  /* back cover */
  .page--back .brand-mark{position:absolute;left:262px;top:188px;width:140px;font-size:34px}
  .company-address{position:absolute;left:229px;top:282px;font-style:normal;font-size:23px;line-height:27px;color:var(--navy)}
  .id-box{position:absolute;height:37px;border:1.5px solid var(--navy);border-radius:6px;background:var(--pale-yellow);text-align:center}
  .id-box__label{position:absolute;left:50%;top:-10px;transform:translateX(-50%);background:var(--white);padding:0 4px;font-size:15px;line-height:16px;white-space:nowrap}
  .id-box__value{display:block;padding-top:6px;font-size:23px;line-height:26px}
  .id-box--reg{left:228px;top:434px;width:227px}
  .id-box--reg .id-box__value{letter-spacing:7px;padding-left:7px}
  .id-box--vat{left:270px;top:507px;width:143px}
  .id-box--vat .id-box__value{font-size:24px}

  /* front cover */
  .proposal-title{position:absolute;left:199px;top:58px;width:260px;text-align:center;font-family:"Oswald",Impact,sans-serif;font-weight:700;font-size:45px;line-height:53px;color:var(--white)}
  .brand-block{position:absolute;left:69px;top:606px;width:241px;text-align:center;color:var(--charcoal)}
  .brand-block .brand-mark{font-size:32px;margin-bottom:26px}
  .brand-block__name{font-weight:700;font-size:20px;letter-spacing:2.2px;line-height:20px}
  .brand-block__ltd{display:flex;align-items:center;gap:6px;font-weight:700;font-size:13px;letter-spacing:5px;line-height:14px;margin-top:1px}
  .brand-block__ltd::before,.brand-block__ltd::after{content:"";flex:1;height:1.5px;background:var(--charcoal)}
  .brand-block__tagline{font-weight:600;font-size:7.5px;letter-spacing:4.3px;line-height:9px;margin-top:3px;white-space:nowrap}
  .partners{position:absolute;left:334px;top:576px;width:118px}
  .partners__label{text-align:center;font-family:"Oswald",sans-serif;font-weight:500;font-size:16px;line-height:18px;letter-spacing:4px;color:var(--charcoal);margin-bottom:6px}
  .partners__grid{height:126px;display:grid;grid-template-columns:62fr 56fr;grid-template-rows:32fr 30fr 30fr 30fr;gap:1.5px;padding:1.5px;background:var(--gold)}
  .partner-badge{background:var(--white);display:flex;align-items:center;justify-content:center;gap:3px}
  .partner-badge--wide{grid-column:1 / 3}
  .badge-shape{display:block}
  .badge-shape--bar{width:34px;height:11px;border-radius:2px}
  .badge-shape--short{width:20px;height:11px;border-radius:2px}
  .badge-shape--circle{width:18px;height:18px;border-radius:50%}
  .badge-shape--square{width:12px;height:12px}
  .page-foot{position:absolute;left:0;bottom:0;width:100%;height:20px;background:linear-gradient(to bottom,#c9ccd6 0,var(--navy) 5px)}
</style>
</head>
<body>
  <div class="spread-divider"></div>
  <h2 class="cover-label cover-label--back">BACK COVER</h2>
  <h2 class="cover-label cover-label--front">FRONT COVER</h2>

  <!-- Back cover -->
  <section class="page page--back">
    <svg class="page-art" viewBox="0 0 993 1404" preserveAspectRatio="none" aria-hidden="true">
      <path fill="var(--green)" d="M575 0 H700 L200 580 L365 360 Z"/>
      <path fill="var(--green)" d="M140 770 Q80 900 150 1020 Q210 1095 330 1150 L700 1320 L783 1404 L220 860 Z"/>
      <path fill="var(--white)" d="M700 0 H993 V1404 H783 L210 860 Q70 720 200 580 Z"/>
    </svg>
    <div class="brand-mark"><span class="brand-mark__dot"></span>Voltline</div>
    <address class="company-address">
      Unit 4B, Larkfield;<br>
      Trade Park<br>
      Larkfield, Ambridge<br>
      Borsetshire, BR7 2QX
    </address>
    <div class="id-box id-box--reg">
      <span class="id-box__label">Registered in England No:</span>
      <span class="id-box__value">20917485</span>
    </div>
    <div class="id-box id-box--vat">
      <span class="id-box__label">Vat Reg No:</span>
      <span class="id-box__value">418 3605 11</span>
    </div>
  </section>

  <!-- Front cover -->
  <section class="page page--front">
    <svg class="page-art" viewBox="0 0 993 1404" preserveAspectRatio="none">
      <defs>
        <radialGradient id="sceneGlow" cx="560" cy="760" r="470" gradientUnits="userSpaceOnUse">
          <stop offset="0" stop-color="#8fb8c8" stop-opacity="0.75"/>
          <stop offset="0.35" stop-color="#5a9f86" stop-opacity="0.6"/>
          <stop offset="0.7" stop-color="#34507e" stop-opacity="0.45"/>
          <stop offset="1" stop-color="#0b1640" stop-opacity="0"/>
        </radialGradient>
      </defs>
      <path fill="var(--yellow)" d="M0 0 H140 C200 40 200 150 170 200 C140 250 80 290 0 345 Z"/>
      <path fill="none" stroke="var(--blue)" stroke-width="4" d="M162 0 C215 50 220 160 190 210 C160 260 100 290 42 330"/>
      <path fill="var(--green)" d="M0 350 L45 300 C70 330 70 380 45 410 L0 440 Z"/>
      <circle cx="262" cy="234" r="7" fill="var(--blue)"/>
      <circle cx="220" cy="277" r="11" fill="var(--blue)"/>
      <circle cx="254" cy="314" r="3" fill="var(--blue)"/>
      <circle cx="183" cy="349" r="13" fill="var(--blue)"/>
      <rect x="0" y="380" width="993" height="660" fill="url(#sceneGlow)"
            role="img" aria-label="Illustration of renewable home energy: wind turbines, solar panel array, large battery, a house with rooftop solar panels, an electric car charging and surrounding trees"/>
      <path fill="var(--yellow)" d="M0 860 C150 950 300 1000 450 1013 C300 1020 150 990 0 935 Z"/>
      <path fill="var(--green)" d="M0 930 C220 1010 480 1015 720 955 L620 990 C400 1070 150 1060 0 1018 Z"/>
      <path fill="var(--white)" d="M0 1018 C150 1060 400 1070 620 990 C800 920 920 780 993 625 V1404 H0 Z"/>
    </svg>
    <h1 class="proposal-title">SALES<br>PROPOSALS</h1>
    <div class="brand-block">
      <div class="brand-mark"><span class="brand-mark__dot"></span>Voltline</div>
      <div class="brand-block__name">VOLTLINE SERVICES</div>
      <div class="brand-block__ltd">LTD</div>
      <div class="brand-block__tagline">ELECTRICAL MECHANICAL RENEWABLE</div>
    </div>
    <div class="partners">
      <div class="partners__label">PARTNERS</div>
      <div class="partners__grid" role="img" aria-label="Partner and accreditation badges">
        <div class="partner-badge partner-badge--wide"><span class="badge-shape badge-shape--bar" style="background:var(--badge-dark)"></span><span class="badge-shape badge-shape--bar" style="background:var(--badge-red)"></span></div>
        <div class="partner-badge"><span class="badge-shape badge-shape--bar" style="background:var(--badge-blue)"></span></div>
        <div class="partner-badge"><span class="badge-shape badge-shape--circle" style="background:var(--navy)"></span></div>
        <div class="partner-badge"><span class="badge-shape badge-shape--bar" style="background:var(--badge-purple)"></span></div>
        <div class="partner-badge"><span class="badge-shape badge-shape--square" style="background:var(--badge-red)"></span><span class="badge-shape badge-shape--short" style="background:var(--badge-dark)"></span></div>
        <div class="partner-badge"><span class="badge-shape badge-shape--bar" style="background:var(--badge-grey)"></span></div>
        <div class="partner-badge"><span class="badge-shape badge-shape--circle" style="background:var(--badge-orange)"></span></div>
      </div>
    </div>
    <div class="page-foot"></div>
  </section>
</body>
</html>
```